Drink Name :Zup Parlo
Flavor:Cola Flavor .
Drink Needs to have a humor and fun in the label . If you look up Zup Parlo on searchly your get the idea of wats the label ideas like link posted below.
Bottle Size is 1.25l and
Made by Torvel LTD Po Box 58193 Wirumoa Auckland NZ .

http://www.fizzlocker.example.nz/crew/kobi-rane-surfer/

Target Market(s)

Young age group 5-30

Industry/Entity Type

Searchly

Requirements
Must have
• Be Modern and cool cola drink .

```html
<!DOCTYPE html>
<html lang="en">
<head>
<meta charset="utf-8">
<title>Zup Parlo – Cola Label</title>
<link rel="stylesheet" href="https://fonts.googleapis.com/css2?family=Nunito:wght@700;800;900&display=swap">
<style>
  :root {
    --canvas: #231f20;
    --label-red: #d42a22;
    --label-red-deep: #a8160f;
    --paper: #ffffff;
    --ink: #1a1a1a;
    --sketch: #e6e6e6;
  }
  html, body { margin: 0; padding: 0; overflow: hidden; }
  body {
    width: 1200px; height: 800px;
    background: var(--canvas);
    font-family: "Nunito", Arial, sans-serif;
    position: relative;
  }
  .label { position: absolute; top: 45px; width: 354px; height: 477px; }
  .label--upright { left: 403px; }
  .label--tilted { left: 805px; }
  .label svg { display: block; width: 100%; height: 100%; }
  .tagline { font-weight: 900; fill: var(--paper); }
  .tagline-accent { fill: var(--ink); }
  .brand-name { font-weight: 900; fill: var(--paper); }
  .descriptor {
    font-weight: 900; fill: var(--label-red);
    stroke: var(--paper); stroke-width: 5px; paint-order: stroke; stroke-linejoin: round;
  }
  .maker { font-weight: 800; fill: var(--paper); font-size: 10.5px; }
  .flavor { font-weight: 800; fill: var(--label-red); font-size: 13px; }
  .volume { font-weight: 800; fill: var(--ink); font-size: 16px; }
  .concept-sketch {
    position: absolute; left: 918px; top: 602px; width: 240px; height: 148px;
    background: linear-gradient(180deg, #f4f4f4, var(--sketch));
  }
</style>
</head>
<body>
  <svg width="0" height="0" style="position:absolute" aria-hidden="true">
    <defs>
      <radialGradient id="label-burst" cx="50%" cy="45%" r="65%">
        <stop offset="0" stop-color="#e2382e"/>
        <stop offset="1" stop-color="#a8160f"/>
      </radialGradient>
    </defs>
  </svg>

  <div class="label label--upright">
    <svg viewBox="0 0 354 477" role="img" aria-label="Zup Parlo cool cola drink label">
      <rect width="354" height="477" fill="var(--paper)"/>
      <path d="M0,78 Q177,-25 354,78 L354,400 Q177,555 0,400 Z" fill="url(#label-burst)"/>
      <text class="tagline" x="44" y="66" font-size="17">be <tspan class="tagline-accent">Modern</tspan></text>
      <text class="brand-name" x="177" y="200" font-size="68" text-anchor="middle">ZUP</text>
      <text class="brand-name" x="177" y="285" font-size="68" text-anchor="middle">PARLO</text>
      <text class="descriptor" x="177" y="372" font-size="29" text-anchor="middle">cool cola drink</text>
      <circle cx="177" cy="420" r="7" fill="var(--paper)"/>
      <text class="maker" x="177" y="438" text-anchor="middle">Made by:</text>
      <text class="maker" x="177" y="450" text-anchor="middle">Torvel LTD, Po Box 58193,</text>
      <text class="maker" x="177" y="462" text-anchor="middle">Wirumoa Auckland NZ .</text>
      <text class="flavor" x="12" y="442" transform="rotate(20 12 442)">Cola Flavor</text>
      <text class="volume" x="294" y="462" transform="rotate(-12 294 462)">1.25l</text>
    </svg>
  </div>

  <div class="label label--tilted">
    <svg viewBox="0 0 354 477" role="img" aria-label="Zup Parlo cool cola drink label, angled name">
      <rect width="354" height="477" fill="var(--paper)"/>
      <path d="M0,78 Q177,-25 354,78 L354,400 Q177,555 0,400 Z" fill="url(#label-burst)"/>
      <text class="tagline" x="58" y="66" font-size="17">be <tspan class="tagline-accent">Modern</tspan></text>
      <g transform="rotate(-42 177 260)">
        <text class="brand-name" x="160" y="250" font-size="56" text-anchor="middle">ZUP PARLO</text>
        <text class="descriptor" x="195" y="298" font-size="27" text-anchor="middle">cool cola drink</text>
      </g>
      <circle cx="177" cy="420" r="7" fill="var(--paper)"/>
      <text class="maker" x="177" y="438" text-anchor="middle">Made by:</text>
      <text class="maker" x="177" y="450" text-anchor="middle">Torvel LTD, Po Box 58193,</text>
      <text class="maker" x="177" y="462" text-anchor="middle">Wirumoa Auckland NZ .</text>
      <text class="flavor" x="12" y="442" transform="rotate(20 12 442)">Cola Flavor</text>
      <text class="volume" x="294" y="462" transform="rotate(-12 294 462)">1.25l</text>
    </svg>
  </div>

  <div class="concept-sketch" role="img" aria-label="Pencil concept sketch of the hand-lettered drink name"></div>
</body>
</html>
```